Offshore Energy Projects Management Consultancy needs a business card design

Logo available. We provide teams to deliver engineering consultancy, project management and delivery teams mainly in the offshore renewables sector. The company is all about bringing the right people to a project to deliver the scope.

The business card will be used for all staff.

The business card should be quite simple, vibrant and uncluttered but convey experience, enthusiasm and integration.

Target Market(s)

Energy Project Developers and Tier 1 construction companies

Contact Information for Business Card

Logo should be on the back of the card. I'm happy for the designer to play with the colour of the logo and background colour.

Front of the card should convey all the must have information in a clear and professional manner but without being overly traditional.

Colors

Designer to choose colors to be used in the design.

Requirements
Must have
• Land Line Tel Number, Mobile Tel Number, Email, business address, web address.

```html
<!DOCTYPE html>
<html lang="en">
<head>
<meta charset="utf-8">
<title>Tidewater Delivery Group – Business Card</title>
<link rel="stylesheet" href="https://fonts.googleapis.com/css2?family=Open+Sans:wght@600;700&display=swap">
<style>
  :root {
    --canvas: #e6e7e8;
    --card: #ffffff;
    --brand-blue: #2f7cc2;
    --sky-blue: #35a7e0;
    --ink-grey: #6d6e71;
    --ink-dark: #3a3a3c;
    --ghost: #ececed;
  }
  * { margin: 0; padding: 0; box-sizing: border-box; }
  html, body { width: 1200px; height: 800px; overflow: hidden; }
  body {
    background: radial-gradient(ellipse at 40% 40%, #f4f4f5 0%, var(--canvas) 60%, #cfd0d2 100%);
    font-family: "Open Sans", Arial, sans-serif;
    position: relative;
  }
  .card {
    position: absolute;
    top: 286px;
    width: 400px;
    height: 228px;
    background: var(--card);
    overflow: hidden;
    box-shadow: 0 6px 14px rgba(0,0,0,0.18);
  }
  .card--back { left: 170px; }
  .card--front { left: 630px; }

  .ghost-circle {
    position: absolute;
    border-radius: 50%;
    border: 26px solid var(--ghost);
  }
  .card--back .ghost-circle { width: 220px; height: 220px; right: -120px; top: -40px; }
  .card--front .ghost-circle { width: 200px; height: 200px; left: -110px; bottom: -110px; }

  .wordmark {
    position: absolute;
    display: flex;
    align-items: center;
    gap: 10px;
    color: var(--ink-grey);
    font-weight: 700;
    text-transform: uppercase;
    line-height: 1.05;
  }
  .wordmark__dot { border-radius: 50%; background: var(--brand-blue); flex: none; }
  .card--back .wordmark { left: 96px; top: 80px; font-size: 22px; letter-spacing: 0.5px; }
  .card--back .wordmark__dot { width: 34px; height: 34px; }
  .card--front .wordmark { left: 30px; top: 28px; font-size: 15px; }
  .card--front .wordmark__dot { width: 22px; height: 22px; }

  .web {
    position: absolute;
    left: 0; right: 0; top: 170px;
    text-align: center;
    font-size: 10px;
    font-weight: 600;
    color: var(--ink-grey);
  }

  .person { position: absolute; right: 36px; top: 32px; text-align: right; }
  .person__name { font-size: 18px; font-weight: 700; color: var(--brand-blue); line-height: 1; }
  .person__role { font-size: 8px; font-weight: 700; color: var(--ink-dark); }

  .contacts {
    position: absolute;
    left: 232px; top: 146px;
    list-style: none;
    font-size: 10px;
    font-weight: 700;
    color: var(--ink-dark);
  }
  .contacts li { display: flex; align-items: center; gap: 9px; height: 14px; }
  .contacts svg { width: 8px; height: 8px; fill: var(--sky-blue); }
</style>
</head>
<body>
  <section class="card card--back" aria-label="Card back">
    <div class="ghost-circle"></div>
    <div class="wordmark">
      <span class="wordmark__dot"></span>
      <span>Tidewater<br>Delivery Group</span>
    </div>
    <p class="web">www. Web address</p>
  </section>

  <section class="card card--front" aria-label="Card front">
    <div class="ghost-circle"></div>
    <div class="wordmark">
      <span class="wordmark__dot"></span>
      <span>Tidewater<br>Delivery Group</span>
    </div>
    <div class="person">
      <p class="person__name">NAME</p>
      <p class="person__role">xxxxxxxxx</p>
    </div>
    <ul class="contacts">
      <li><svg viewBox="0 0 10 10"><path d="M5 0a3.5 3.5 0 0 0-3.5 3.5C1.5 6 5 10 5 10s3.5-4 3.5-6.5A3.5 3.5 0 0 0 5 0zm0 5a1.5 1.5 0 1 1 0-3 1.5 1.5 0 0 1 0 3z"/></svg>Address</li>
      <li><svg viewBox="0 0 10 10"><path d="M1 3q4-3 8 0v1.5H7V3.5H3v1H1zM2 5h6l1 4H1z"/></svg>Landline no.</li>
      <li><svg viewBox="0 0 10 10"><path d="M3 0h4a1 1 0 0 1 1 1v8a1 1 0 0 1-1 1H3a1 1 0 0 1-1-1V1a1 1 0 0 1 1-1zm0 1.5v6h4v-6z"/></svg>Mobile no.</li>
      <li><svg viewBox="0 0 10 10"><path d="M0 2h10v6H0zm1 1v.3l4 2.5 4-2.5V3z"/></svg>Email ID</li>
    </ul>
  </section>
</body>
</html>
```